Business Card - Harlow Birch

Need Business Card design for company named Harlow Birch. Software development focused mainly on Ardel eKallo & oBix Apps. I've attached our logo with both a black and white background. Please add trademark symbol to logo when using.

```html
<!DOCTYPE html>
<html lang="en">
<head>
<meta charset="utf-8">
<title>Harlow Birch – Business Card</title>
<link rel="stylesheet" href="https://fonts.googleapis.com/css2?family=Ubuntu:wght@500&family=Roboto+Condensed:wght@700&display=swap">
<style>
  :root {
    --canvas: #e9e7e4;
    --charcoal: #333333;
    --paper: #ffffff;
    --yellow: #f7c114;
    --orange: #f59a33;
    --red: #d71f26;
    --ink: #2f2f2f;
  }
  * { box-sizing: border-box; margin: 0; padding: 0; }
  html, body { width: 1200px; height: 1000px; overflow: hidden; }
  body {
    background: var(--canvas);
    display: flex;
    align-items: center;
    justify-content: center;
    gap: 60px;
  }
  .card {
    position: relative;
    width: 380px;
    height: 660px;
    overflow: hidden;
    box-shadow: 0 10px 30px rgba(0,0,0,0.18);
  }
  .card--front { background: var(--charcoal); }
  .card--back { background: var(--paper); }

  .brand {
    position: absolute;
    left: 0; right: 0;
    text-align: center;
    font-family: "Ubuntu", sans-serif;
    font-weight: 500;
    font-size: 44px;
    letter-spacing: -0.5px;
  }
  .brand sup { font-size: 16px; vertical-align: 22px; margin-left: 4px; }
  .card--front .brand { top: 250px; color: var(--paper); }
  .card--back .brand { top: 150px; color: var(--ink); }

  .contact {
    position: absolute;
    left: 36px;
    top: 250px;
    font-family: "Roboto Condensed", sans-serif;
    font-weight: 700;
    font-size: 23px;
    line-height: 1.4;
    color: var(--ink);
  }
  .contact .accent-yellow { color: var(--yellow); }
  .contact .accent-orange { color: var(--orange); }
  .contact .accent-red { color: var(--red); }

  .stripes {
    position: absolute;
    left: 0; right: 0; bottom: 0;
    background: var(--charcoal);
    padding-bottom: 56px;
  }
  .card--front .stripes { top: 430px; }
  .card--back .stripes { top: 440px; }
  .stripe { height: 50px; margin-bottom: 12px; }
  .stripe--yellow { background: var(--yellow); }
  .stripe--orange { background: var(--orange); }
  .stripe--red { background: var(--red); }
</style>
</head>
<body>
  <section class="card card--front" aria-label="Card front">
    <div class="brand">Harlow Birch<sup>™</sup></div>
    <div class="stripes">
      <div class="stripe stripe--yellow"></div>
      <div class="stripe stripe--orange"></div>
      <div class="stripe stripe--red"></div>
    </div>
  </section>

  <section class="card card--back" aria-label="Card back">
    <div class="brand">Harlow Birch<sup>™</sup></div>
    <div class="contact">
      <p>218 Elm Ridge Rd, Dunmore, <span class="accent-yellow">FL 34021</span></p>
      <p>Mobile: <span class="accent-orange">555-201-4478</span></p>
      <p>Fax: <span class="accent-red">555-201-4479</span></p>
    </div>
    <div class="stripes">
      <div class="stripe stripe--yellow"></div>
      <div class="stripe stripe--orange"></div>
      <div class="stripe stripe--red"></div>
    </div>
  </section>
</body>
</html>
```